Simple graphic for a book or slide presentation

We are looking for a style that suits the style of our book. It's title is Harbor. Keeping a calm course through stormy seas. There will be more line drawing/graphics in the book but how you design this image will create the style for all the other simple graphics in the book (once we decide what they are). So this one design will lead to a few more to match the style of this one. We'd like the shape of the overall graphic (i.e the arrows and words/bubbles) to be circular (not a rounded square as appears in the sample attached). Perhaps the words don't need to be in ovals or bound by anything at all; perhaps they do - let's see what you see. We'd like you to choose a font or offer many different fonts you think will capture the practical yet unconventional tone of the book. The book is teaching that managing risks in life is a life-skill that can be learned. The section of the book where this graphic will be placed is called "the power of language" - basically we are saying that thoughts, words and actions create our culture and our destiny. This insight comes from Torvel Pelloru's famous quote:
Carefully watch your thoughts, for they become your words.
Manage and watch your words, for they will become your actions.
Consider and judge your actions, for they have become your habits.
Acknowledge and watch your habits, for they shall become your values.
Understand and embrace your values, for they become your destiny.

Please change the text in the middle of the graphic to say: The Human Culture Cycle

```html
<!DOCTYPE html>
<html lang="en">
<head>
<meta charset="utf-8">
<title>The Human Culture Cycle</title>
<link rel="stylesheet" href="https://fonts.googleapis.com/css2?family=Roboto:wght@700&display=swap">
<style>
  :root {
    --ink: #333333;
    --paper: #ffffff;
    --frame: #4a4a4a;
  }
  html, body {
    margin: 0;
    padding: 0;
    width: 1200px;
    height: 1200px;
    overflow: hidden;
    background: var(--paper);
  }
  .canvas {
    box-sizing: border-box;
    width: 1200px;
    height: 1200px;
    border: 2px solid var(--frame);
    background: var(--paper);
  }
  .cycle-diagram {
    display: block;
    width: 100%;
    height: 100%;
  }
  .cycle-arrow {
    fill: var(--paper);
    stroke: var(--ink);
    stroke-width: 5;
    stroke-linejoin: miter;
  }
  .hub-ring {
    fill: var(--paper);
    stroke: var(--ink);
    stroke-width: 5;
  }
  .arrow-label {
    font-family: "Roboto", Arial, sans-serif;
    font-weight: 700;
    font-size: 34px;
    letter-spacing: 1.5px;
    fill: var(--ink);
  }
  .hub-title {
    font-family: "Roboto", Arial, sans-serif;
    font-weight: 700;
    font-size: 43px;
    letter-spacing: 1.5px;
    fill: var(--ink);
  }
</style>
</head>
<body>
<div class="canvas">
  <svg class="cycle-diagram" viewBox="0 0 1200 1200" xmlns="http://www.w3.org/2000/svg" role="img" aria-label="The Human Culture Cycle: culture, thoughts, words, actions, habits, values">
    <defs>
      <path id="arrow-shape" d="M321.5 443 A332 332 0 0 1 534.3 285.5 L527.5 256.3 L593.5 312.4 L556.6 382 L550 353.7 A262 262 0 0 0 382.1 478 L368.7 434.4 Z"/>
      <path id="label-track-cw" d="M357.1 451.6 A297 297 0 0 1 562.5 315.7" fill="none"/>
      <path id="label-track-ccw" d="M562.5 315.7 A297 297 0 0 0 357.1 451.6" fill="none"/>
    </defs>

    <g class="cycle-step">
      <use href="#arrow-shape" class="cycle-arrow"/>
      <text class="arrow-label" dy="12"><textPath href="#label-track-cw" startOffset="50%" text-anchor="middle">CULTURE</textPath></text>
    </g>
    <g class="cycle-step" transform="rotate(60 609 609)">
      <use href="#arrow-shape" class="cycle-arrow"/>
      <text class="arrow-label" dy="12"><textPath href="#label-track-cw" startOffset="50%" text-anchor="middle">THOUGHTS</textPath></text>
    </g>
    <g class="cycle-step" transform="rotate(120 609 609)">
      <use href="#arrow-shape" class="cycle-arrow"/>
      <text class="arrow-label" dy="12"><textPath href="#label-track-cw" startOffset="50%" text-anchor="middle">WORDS</textPath></text>
    </g>
    <g class="cycle-step" transform="rotate(180 609 609)">
      <use href="#arrow-shape" class="cycle-arrow"/>
      <text class="arrow-label" dy="12"><textPath href="#label-track-ccw" startOffset="50%" text-anchor="middle">ACTIONS</textPath></text>
    </g>
    <g class="cycle-step" transform="rotate(240 609 609)">
      <use href="#arrow-shape" class="cycle-arrow"/>
      <text class="arrow-label" dy="12"><textPath href="#label-track-ccw" startOffset="50%" text-anchor="middle">HABITS</textPath></text>
    </g>
    <g class="cycle-step" transform="rotate(300 609 609)">
      <use href="#arrow-shape" class="cycle-arrow"/>
      <text class="arrow-label" dy="12"><textPath href="#label-track-ccw" startOffset="50%" text-anchor="middle">VALUES</textPath></text>
    </g>

    <circle class="hub-ring" cx="609" cy="609" r="165"/>
    <text class="hub-title" text-anchor="middle">
      <tspan x="609" y="545">THE</tspan>
      <tspan x="609" y="598">HUMAN</tspan>
      <tspan x="609" y="652">CULTURE</tspan>
      <tspan x="609" y="705">CYCLE</tspan>
    </text>
  </svg>
</div>
</body>
</html>
```